名刺の背景は、白地(裏地デザインは、ありもOK)
複数の色味というよりは、シンプルな色使い

シンプルだけど、上品さを感じるもの

株式会社plumeridge/代表取締役/名前/読みがな(英語)/住所/電話番号/mail address/HP URL
シンプル 複雑
単色 カラフル
暗い 明るい
日常 高級
遊び心 厳粛
未来的 伝統的
女性的 男性的
緑系、グレー系、色は絶対ではありませんので、イメージやデザインに添ってご提案いただけるのであれば嬉しいです
• 高解像度JPG (.jpg)
• イラストレーター形式 (.ai)
• フォトショップ形式 (.psd)
• PNG形式 (.png)
現在の色味が、添付ファイルの名刺の色なので、参考にしていただけると嬉しいです。
緑というよりは、エメラルドグリーンのような色味です。
※添付ファイルに記載されている、個人情報は名刺サンプルに記載しないでください。
お手数ですがよろしくお願いいたします。
※社名は「株式会社plumeridge」のみで、「inc.」は無しでお願いいたします。
たくさんのご提案ありがとうございます!
デザインが一般企業よりのものを探しており、可能であれば、
もう少しデザインを拝見したく、延長させていただきました。

お忙しいところお手数ですが、どうぞよろしくお願いいたします。

デザイン性が一番高かったためです。

たくさんのご提案、ありがとうございました!
ご丁寧にご対応いただき、とても助かりました。
また依頼あれば出させていただきます。

```html
<!DOCTYPE html>
<html lang="ja">
<head>
<meta charset="utf-8">
<title>plumeridge business card</title>
<link rel="stylesheet" href="https://fonts.googleapis.com/css2?family=Exo+2:wght@200;300;400&family=Noto+Serif+JP:wght@400;500&family=Roboto:wght@400;500&display=swap">
<style>
  :root {
    --stage: #d9d9d9;
    --paper: #ffffff;
    --accent: #1e9bc4;
    --back: #1f6f78;
    --back-faint: #3a8690;
    --ink: #333333;
    --label: #444444;
  }
  * { margin: 0; padding: 0; box-sizing: border-box; }
  html, body { width: 805px; height: 1200px; overflow: hidden; }
  body { background: var(--stage); position: relative; font-family: "Roboto", sans-serif; }

  .side-label { position: absolute; left: 52px; font: 400 19px "Roboto", sans-serif; color: var(--label); }
  .side-label--front { top: 74px; }
  .side-label--back { top: 628px; }

  .card { position: absolute; left: 40px; width: 725px; height: 438px; overflow: hidden; }
  .card--front { top: 118px; background: var(--paper); box-shadow: 0 1px 3px rgba(0,0,0,.15); }
  .card--back { top: 675px; background: var(--back); }

  .accent-bar { position: absolute; left: 0; top: 40px; width: 18px; height: 190px; background: var(--accent); }

  .person { position: absolute; left: 48px; top: 140px; color: var(--ink); }
  .person__title { font: 400 15px "Noto Serif JP", serif; }
  .person__name { font: 500 32px "Noto Serif JP", serif; letter-spacing: 2px; margin-top: 8px; }
  .person__roman { font: 400 15px "Noto Serif JP", serif; margin-top: 8px; }
  .person__mobile { display: flex; align-items: center; gap: 6px; font: 400 17px "Roboto", sans-serif; margin-top: 36px; }

  .brand { position: absolute; left: 360px; top: 145px; text-align: center; color: var(--accent); }
  .brand__kind { font: 400 12px "Noto Serif JP", serif; }
  .brand__name { display: flex; align-items: center; gap: 8px; font: 300 27px "Exo 2", sans-serif; }
  .brand__dot { width: 10px; height: 10px; border-radius: 50%; background: var(--accent); }

  .company { position: absolute; left: 335px; top: 262px; color: var(--accent); }
  .company__name { font: 400 25px "Exo 2", sans-serif; }
  .contact { list-style: none; margin-top: 6px; }
  .contact__item { display: flex; align-items: center; gap: 8px; font: 400 15px "Roboto", sans-serif; color: var(--ink); line-height: 27px; }
  .company__url { font: 500 16px "Roboto", sans-serif; margin-top: 14px; }

  .icon { width: 16px; height: 16px; flex: none; }

  .back__row { position: absolute; left: 40px; right: 40px; display: flex; justify-content: space-between; font: 200 110px "Exo 2", sans-serif; color: var(--back-faint); line-height: 1; }
  .back__row--top { top: 45px; }
  .back__row--bottom { top: 260px; }
  .back__name { position: absolute; left: 0; right: 0; top: 190px; text-align: center; font: 300 31px "Exo 2", sans-serif; color: #ffffff; }
</style>
</head>
<body>
  <p class="side-label side-label--front">Front</p>
  <section class="card card--front">
    <div class="accent-bar"></div>
    <div class="person">
      <p class="person__title">代表取締役</p>
      <p class="person__name">佐野 綾子</p>
      <p class="person__roman">Ayako Sano</p>
      <p class="person__mobile">
        <svg class="icon" viewBox="0 0 16 16"><rect width="16" height="16" rx="2" fill="var(--accent)"/><rect x="5" y="2.5" width="6" height="11" rx="1" fill="none" stroke="#fff" stroke-width="1.4"/></svg>
        090-0000-0000
      </p>
    </div>
    <div class="brand">
      <p class="brand__kind">株式会社</p>
      <p class="brand__name"><span class="brand__dot"></span>plumeridge</p>
    </div>
    <div class="company">
      <p class="company__name">plumeridge</p>
      <ul class="contact">
        <li class="contact__item">
          <svg class="icon" viewBox="0 0 16 16"><rect width="16" height="16" rx="2" fill="var(--accent)"/><path d="M3 8 8 3.5 13 8M4.5 7v5.5h7V7" fill="none" stroke="#fff" stroke-width="1.4"/></svg>
          4-5-6 nishiharu,Minato-ku,Tokyo
        </li>
        <li class="contact__item">
          <svg class="icon" viewBox="0 0 16 16"><rect width="16" height="16" rx="2" fill="var(--accent)"/><path d="M4.5 3.5c0 5 3 8 8 8l.5-2-2.5-1-1 1c-1.5-.7-2.3-1.5-3-3l1-1-1-2.5z" fill="#fff"/></svg>
          000-0000-0000
        </li>
        <li class="contact__item">
          <svg class="icon" viewBox="0 0 16 16"><rect width="16" height="16" rx="2" fill="var(--accent)"/><rect x="3" y="4.5" width="10" height="7" fill="none" stroke="#fff" stroke-width="1.3"/><path d="M3 4.5 8 8.5 13 4.5" fill="none" stroke="#fff" stroke-width="1.3"/></svg>
          info@example.com
        </li>
      </ul>
      <p class="company__url">http://www.example.com</p>
    </div>
  </section>

  <p class="side-label side-label--back">Back</p>
  <section class="card card--back">
    <div class="back__row back__row--top"><span>p</span><span>l</span><span>u</span><span>m</span><span>e</span></div>
    <p class="back__name">plumeridge</p>
    <div class="back__row back__row--bottom"><span>r</span><span>i</span><span>d</span><span>g</span><span>e</span></div>
  </section>
</body>
</html>
```